Townhome Multi-Family Property Exterior Sign

Hello. We are looking for a new design for our exterior pylon for for a multi-family housing property in Texas. The design will need to go on a new sign panel to replace the existing (see photo of existing). We are looking to see both modern and contemporary designs. Included the sign should be the name, Loma Brisa Townhomes and the web address www.lomabrisatownhomes.example.

Attached here is a PDF file of the proposed new sign shape. We are open to other shape ideas as well if your design would better suit a more rectangular shape.

Industry/Entity Type

Property

Font styles to use
Serif
Sans Serif

Colors
9bcb3c

Requirements
Must have
• Name of building: Loma Brisa Townhomes
• Website: www.lomabrisatownhomes.example
Nice to have
• Address: 420-530 Halvorsen Lane (only if it fits nicely)

```html
<!DOCTYPE html>
<html lang="en">
<head>
<meta charset="utf-8">
<title>Loma Brisa Townhomes – Exterior Sign</title>
<link rel="stylesheet" href="https://fonts.googleapis.com/css2?family=Vollkorn:wght@700;800&display=swap">
<style>
  :root {
    --backdrop: #e6e6e4;
    --pylon: #393939;
    --pylon-edge: #222222;
    --brand-green: #217346;
    --brand-green-edge: #1a4a30;
    --title-shadow: #0f3320;
    --plaque: #ffffff;
    --ink-green: #1f5a36;
    --title-white: #ffffff;
  }
  html, body {
    margin: 0;
    padding: 0;
    overflow: hidden;
  }
  body {
    width: 1200px;
    height: 729px;
    background: var(--backdrop);
  }
  .sign {
    display: block;
    width: 1200px;
    height: 729px;
  }
  .pylon { fill: var(--pylon); }
  .pylon-edge { fill: var(--pylon-edge); }
  .name-band { fill: var(--brand-green); }
  .name-band-edge { fill: var(--brand-green-edge); }
  .info-plaque { fill: var(--plaque); }
  .property-name {
    font-family: "Vollkorn", Georgia, serif;
    font-weight: 800;
    font-size: 98px;
    fill: var(--title-white);
  }
  .property-name-shadow {
    font-family: "Vollkorn", Georgia, serif;
    font-weight: 800;
    font-size: 98px;
    fill: var(--title-shadow);
  }
  .contact-line {
    font-family: "Vollkorn", Georgia, serif;
    font-weight: 700;
    font-size: 26px;
    fill: var(--ink-green);
  }
</style>
</head>
<body>
<svg class="sign" viewBox="0 0 1200 729" xmlns="http://www.w3.org/2000/svg" role="img" aria-label="Loma Brisa Townhomes pylon sign">
  <!-- pylon body -->
  <path class="pylon-edge" d="M280 50 Q706 55 934 172 V692 H280 Z"/>
  <path class="pylon" d="M274 45 Q700 50 928 167 V686 H274 Z"/>

  <!-- name band -->
  <rect class="name-band-edge" x="209" y="222" width="792" height="271"/>
  <rect class="name-band" x="202" y="216" width="792" height="271"/>

  <g text-anchor="middle">
    <text class="property-name-shadow" x="601" y="346" textLength="651" lengthAdjust="spacingAndGlyphs">LOMA BRISA</text>
    <text class="property-name" x="598" y="343" textLength="651" lengthAdjust="spacingAndGlyphs">LOMA BRISA</text>
    <text class="property-name-shadow" x="601" y="432" textLength="651" lengthAdjust="spacingAndGlyphs">TOWNHOMES</text>
    <text class="property-name" x="598" y="429" textLength="651" lengthAdjust="spacingAndGlyphs">TOWNHOMES</text>
  </g>

  <!-- contact plaque -->
  <rect class="info-plaque" x="303" y="491" width="585" height="126"/>
  <g text-anchor="middle">
    <text class="contact-line" x="596" y="545" textLength="501" lengthAdjust="spacingAndGlyphs">www.LomaBrisaTownhomes.example</text>
    <text class="contact-line" x="596" y="586" textLength="350" lengthAdjust="spacingAndGlyphs">420-530 Halvorsen Lane</text>
  </g>
</svg>
</body>
</html>
```